Design a New Business Card for Our Company

We are looking for fresh, unique, and a modern business card that reflects our roots as digital marketing agency focused on SEM.

Industry/Entity Type

Marketing

Contact Information for Business Card

looking for very unique out of the box designs. clean and modern that compliments our logo

Requirements
Must have
• colors should match our logo
• Front should have name, address, email, and phone/fax of the person, phone/fax are the same number
• back should have our url

```html
<!DOCTYPE html>
<html lang="en">
<head>
<meta charset="utf-8">
<title>Clearpath Solutions – Business Card</title>
<link rel="stylesheet" href="https://fonts.googleapis.com/css2?family=Source+Sans+3:wght@400;600&display=swap">
<style>
  :root {
    --backdrop: #4b3139;
    --card-light: #ffffff;
    --card-dark: #231f20;
    --accent-blue: #5b95cf;
    --soft-grey: #b3b3b3;
    --text-grey: #58595b;
    --url-grey: #bcbec0;
  }
  * { margin: 0; padding: 0; box-sizing: border-box; }
  html, body {
    width: 1200px; height: 1200px; overflow: hidden;
    background: var(--backdrop);
    font-family: "Source Sans 3", sans-serif;
  }
  .canvas { position: relative; width: 1200px; height: 1200px; }
  .card {
    position: absolute; left: 226px; width: 748px; height: 424px;
    overflow: hidden;
    box-shadow: 0 4px 14px rgba(0,0,0,0.35);
  }
  .card--front { top: 149px; background: var(--card-light); }
  .card--back { top: 628px; background: var(--card-dark); }

  .edge-dot {
    position: absolute; left: -29px; top: 169px;
    width: 58px; height: 58px; border-radius: 50%;
    background: var(--accent-blue);
  }
  .decor-field {
    position: absolute; right: 0; top: 0; width: 330px; height: 424px;
    background: radial-gradient(circle at 60% 50%, rgba(255,255,255,0) 0 30%, rgba(179,179,179,0.35) 45%, rgba(91,149,207,0.45) 80%);
  }
  .contact { position: absolute; left: 40px; top: 170px; color: var(--text-grey); }
  .contact__name {
    font-size: 28px; font-weight: 400; color: var(--accent-blue); line-height: 1;
  }
  .contact__title { font-size: 19px; margin-top: 8px; line-height: 1; }
  .contact__address { font-size: 19px; line-height: 26px; margin-top: 24px; }
  .contact__lines { list-style: none; margin-top: 18px; }
  .contact__lines li {
    display: flex; align-items: center; gap: 10px;
    font-size: 19px; line-height: 25px;
  }
  .contact__lines svg { width: 18px; height: 16px; fill: var(--accent-blue); flex: none; }

  .brand {
    position: absolute; left: 0; right: 0; top: 168px;
    display: flex; align-items: center; justify-content: center; gap: 18px;
  }
  .brand__mark { width: 58px; height: 58px; border-radius: 50%; background: var(--accent-blue); }
  .brand__name { font-size: 56px; font-weight: 600; color: var(--soft-grey); letter-spacing: -0.5px; }
  .url {
    position: absolute; left: 0; right: 0; top: 376px; text-align: center;
    font-size: 19px; color: var(--url-grey);
  }
  .url__domain { color: var(--accent-blue); }
</style>
</head>
<body>
<main class="canvas">
  <section class="card card--front">
    <div class="edge-dot"></div>
    <div class="decor-field" role="img" aria-label="Decorative arrangement of grey and blue circles"></div>
    <div class="contact">
      <h1 class="contact__name">Marcus Ellery</h1>
      <p class="contact__title">Managing Partner</p>
      <p class="contact__address">2218 Alder Row<br>Brookfield, NC 27690</p>
      <ul class="contact__lines">
        <li><svg viewBox="0 0 18 16"><path d="M1 3h16v10H1z" fill="none" stroke="#5b95cf" stroke-width="1.6"/><path d="M1 3l8 6 8-6" fill="none" stroke="#5b95cf" stroke-width="1.6"/></svg>mellery@clearpathsolutions.com</li>
        <li><svg viewBox="0 0 18 16"><path d="M1 6c0-3 4-4 8-4s8 1 8 4v1h-4V5H5v2H1z"/><path d="M4 8h10l2 7H2z"/><circle cx="9" cy="11.5" r="2" fill="#fff"/></svg>919-555-0186</li>
        <li><svg viewBox="0 0 18 16"><path d="M5 1h8v4H5z"/><path d="M1 6h16v6h-3v-2H4v2H1z"/><path d="M5 11h8v4H5z"/></svg>919-555-0186</li>
      </ul>
    </div>
  </section>

  <section class="card card--back">
    <div class="brand">
      <span class="brand__mark"></span>
      <span class="brand__name">Clearpath Solutions</span>
    </div>
    <p class="url">www.<span class="url__domain">clearpathsolutions</span>.com</p>
  </section>
</main>
</body>
</html>
```